Schnapsbrennerei sucht neue Etiketten
Zielgruppe
Wir sind eine örtliche Schnapsbrennerei, die inzwischen seit ein paar Jahren einen eigenen Kundenstamm aufgebaut hat. Nun werden wir im nächsten Jahr einen neuen Verkaufsraum bauen. Aus diesem Grund wollen wir unsere Etiketten komplett überarbeiten.
Ein neues Logo habe ich bereits designen lassen. Diese finden Sie unten im Dokumententenupload. Wir legen viel Wert auf eine sehr hohe Qualität, welche sich sowohl in unserem Logo als auch den Etiketten Wiederspiegeln soll.
Unsere Kundschaft ist hauptsächlich Ü35 und legt viel Wert auf hochwertige Produkte.
Aufgabenstellung
Eines direkt vorne weg: Da wir unsere komplette Produktpalette neu gestalten wollen würde ich Sie bitten, der Einfachheit halber zuerst nur ein Schnapsetikett (z.B. Zwetschge oder Willi), ein Likör Etikett und ein Etikett für unseren Whiskey zu erstellen.
Darüber hinaus bitte ich Sie auch ein Design für unseren neuen Gin und einen Aquavit, welcher im Herbst auf den Markt kommen soll zu designen. Im Anschluss daran, werde ich in der Zusammenarbeit mit Ihnen die Etiketten optimieren wollen.
Sobald ein 'Grundetikett' entstanden ist, sollen dann auch die anderen Schnäpse und Liköre in dem gleichen Stil erstellt werden. Explizit möchte ich daraufhin weisen, dass sowohl die Whiskeys als auch der Gin und der Aquavit nicht zwangsläufig das gleiche 'Grundetikett' wie der Schnaps und der Likör haben sollen. Ist bei unseren aktuellen Etiketten auch nicht der Fall. Sehen Sie in den Bildern unten.
Wir verkaufen unseren Schnaps und Likör in 3 unterschieldichen Größen 0,2; 0,5 und 1,0 Liter. Wir verwenden für die 0,2 und 0,5 die Flasche Tessa. Das Etikett der 0,5er Flasche soll in etwa 65x120-130 mm sein. Hier sind wir allerdings variabel.
Dieses entstandene Etikett soll dann auf die anderen Flaschen entsprechend angepasst werden.
Sie finden im Dokumentenupload unsere aktuellen Etiketten und das Logo, welches eingebaut werden soll. Auch ein Etikett von einem örtlichen Weingut, welches mir vom Aufbau und der Unterteilung sehr gut gefällt, werde ich mit anhängen. Allerdings ist dieses Bild sehr unscharf. Wie gesagt es geht hierbei hauptsächlich um die Einteilung mit den oberen und den unteren 'Rahmen'.
Auch unsere Preisliste finden Sie Anhang, wobei diese noch in der Rohform ist und das Obst so nicht verwendet wird, aber hier sind die meisten Produkte drauf.
Das Logo gibt es in verschiedenen Farben. Gerne dürfen Sie für die unterschiedlichen Produkte auch unterschiedliche Farben nutzen.
Was ich mir persönlich g..

```html
<!DOCTYPE html>
<html lang="de">
<head>
<meta charset="utf-8">
<title>Hollberg's Landbrennerei – Etiketten</title>
<link href="https://fonts.googleapis.com/css2?family=Lato:wght@400;700&family=Dancing+Script:wght@500&display=swap" rel="stylesheet">
<style>
  :root{
    --ink:#222;
    --plum:#4a1a4f; --plum-light:#9a6d9c;
    --orange:#ee7203; --orange-light:#f9a441;
    --berry:#5a1822; --berry-light:#a4636c;
    --coal:#1c1c1c; --silver:#d6d6d6; --slate:#5a5a5a; --mist:#a9a9a9;
    --gold:#e8a33b;
    --amber-a:#f3a772; --amber-b:#c8683a;
    --whisky-a:#f07a1e; --whisky-b:#a8440f;
  }
  html,body{margin:0;padding:0;}
  body{width:848px;height:1200px;overflow:hidden;background:#fff;position:relative;font-family:'Lato',sans-serif;color:var(--ink);}
  .section-title{position:absolute;left:50px;margin:0;font-size:17px;font-weight:400;}
  .label{position:absolute;display:block;}
  .label text{font-family:'Lato',sans-serif;}
  .label .script{font-family:'Dancing Script',cursive;}
  .liquor{width:176px;height:325px;}
  .whisky{width:208px;height:208px;}
  .gin{width:282px;height:282px;left:50px;top:845px;}
  .mockup{position:absolute;}
  .mockup--liquor{top:74px;width:66px;height:282px;border-radius:30px 30px 8px 8px;background:linear-gradient(180deg,#2a2a2a 0 12%,#eee 12% 24%,var(--amber-a) 40%,var(--amber-b));}
  .mockup--whisky{top:491px;width:109px;height:284px;border-radius:14px;background:linear-gradient(180deg,#1d1d1d 0 22%,var(--whisky-a) 36%,var(--whisky-b));}
  .mockup--gin{left:416px;top:849px;width:373px;height:281px;background:linear-gradient(180deg,#fafafa,#e9e9e9);}
</style>
</head>
<body>

<h2 class="section-title" style="top:22px">Liköre/Schnäpse:</h2>

<!-- liquor labels -->
<svg class="label liquor" style="left:49px;top:58px" viewBox="0 0 340 630" preserveAspectRatio="none">
  <rect width="340" height="630" fill="#fff"/>
  <polygon points="0,0 340,0 340,115 0,160" fill="var(--plum)"/>
  <polygon points="30,160 340,118 340,140 30,182" fill="var(--plum-light)"/>
  <circle cx="170" cy="55" r="16" fill="#fff"/>
  <text x="170" y="102" text-anchor="middle" fill="#fff" font-size="16" font-weight="700" letter-spacing="3">HOLLBERG'S</text>
  <text x="22" y="250" fill="var(--plum)" font-size="26" transform="rotate(-7 22 250)">HOLLBERG'S</text>
  <polygon points="0,270 340,225 340,238 0,282" fill="var(--plum-light)"/>
  <polygon points="0,282 340,238 340,365 0,402" fill="var(--plum)"/>
  <text class="script" x="25" y="358" fill="#fff" font-size="76" transform="rotate(-7 25 358)">Pflaume</text>
  <text x="30" y="430" fill="var(--plum)" font-size="20" transform="rotate(-7 30 430)">40 % VOL</text>
  <text x="315" y="395" text-anchor="end" fill="var(--plum)" font-size="20" transform="rotate(-7 315 395)">0,2 L</text>
  <polygon points="0,505 340,462 340,475 0,520" fill="var(--plum-light)"/>
  <polygon points="0,520 340,475 340,630 0,630" fill="var(--plum)"/>
  <text x="170" y="590" text-anchor="middle" fill="#fff" font-size="13">Edelbrände &amp; Liköre Konrad Hollberg</text>
  <text x="170" y="607" text-anchor="middle" fill="#fff" font-size="12">Lindenweg 12 · D-97999 Auheim · Telefon 0 12 34 - 56 78</text>
</svg>

<svg class="label liquor" style="left:138px;top:72px;transform:rotate(8deg)" viewBox="0 0 340 630" preserveAspectRatio="none">
  <rect width="340" height="630" fill="#fff"/>
  <polygon points="0,0 340,0 340,115 0,160" fill="var(--orange)"/>
  <polygon points="30,160 340,118 340,140 30,182" fill="var(--orange-light)"/>
  <circle cx="170" cy="55" r="16" fill="#fff"/>
  <text x="170" y="102" text-anchor="middle" fill="#fff" font-size="16" font-weight="700" letter-spacing="3">HOLLBERG'S</text>
  <text x="22" y="250" fill="var(--orange)" font-size="26" transform="rotate(-7 22 250)">HOLLBERG'S</text>
  <polygon points="0,270 340,225 340,238 0,282" fill="var(--orange-light)"/>
  <polygon points="0,282 340,238 340,365 0,402" fill="var(--orange)"/>
  <text class="script" x="25" y="358" fill="#fff" font-size="76" transform="rotate(-7 25 358)">Maracuja</text>
  <text x="30" y="430" fill="var(--orange)" font-size="20" transform="rotate(-7 30 430)">40 % VOL</text>
  <text x="315" y="395" text-anchor="end" fill="var(--orange)" font-size="20" transform="rotate(-7 315 395)">0,2 L</text>
  <polygon points="0,505 340,462 340,475 0,520" fill="var(--orange-light)"/>
  <polygon points="0,520 340,475 340,630 0,630" fill="var(--orange)"/>
  <text x="170" y="590" text-anchor="middle" fill="#fff" font-size="13">Edelbrände &amp; Liköre Konrad Hollberg</text>
  <text x="170" y="607" text-anchor="middle" fill="#fff" font-size="12">Lindenweg 12 · D-97999 Auheim · Telefon 0 12 34 - 56 78</text>
</svg>

<svg class="label liquor" style="left:234px;top:71px;transform:rotate(2.5deg)" viewBox="0 0 340 630" preserveAspectRatio="none">
  <rect width="340" height="630" fill="#fff"/>
  <polygon points="0,0 340,0 340,115 0,160" fill="var(--berry)"/>
  <polygon points="30,160 340,118 340,140 30,182" fill="var(--berry-light)"/>
  <circle cx="170" cy="55" r="16" fill="#fff"/>
  <text x="170" y="102" text-anchor="middle" fill="#fff" font-size="16" font-weight="700" letter-spacing="3">HOLLBERG'S</text>
  <text x="22" y="250" fill="var(--berry)" font-size="26" transform="rotate(-7 22 250)">HOLLBERG'S</text>
  <polygon points="0,270 340,225 340,238 0,282" fill="var(--berry-light)"/>
  <polygon points="0,282 340,238 340,365 0,402" fill="var(--berry)"/>
  <text class="script" x="25" y="352" fill="#fff" font-size="58" textLength="295" lengthAdjust="spacingAndGlyphs" transform="rotate(-7 25 352)">Johannisbeere</text>
  <text x="30" y="430" fill="var(--berry)" font-size="20" transform="rotate(-7 30 430)">40 % VOL</text>
  <text x="315" y="395" text-anchor="end" fill="var(--berry)" font-size="20" transform="rotate(-7 315 395)">0,2 L</text>
  <polygon points="0,505 340,462 340,475 0,520" fill="var(--berry-light)"/>
  <polygon points="0,520 340,475 340,630 0,630" fill="var(--berry)"/>
  <text x="170" y="590" text-anchor="middle" fill="#fff" font-size="13">Edelbrände &amp; Liköre Konrad Hollberg</text>
  <text x="170" y="607" text-anchor="middle" fill="#fff" font-size="12">Lindenweg 12 · D-97999 Auheim · Telefon 0 12 34 - 56 78</text>
</svg>

<div class="mockup mockup--liquor" style="left:443px" role="img" aria-label="Flasche mit Pflaume-Etikett"></div>
<div class="mockup mockup--liquor" style="left:538px" role="img" aria-label="Flasche mit Maracuja-Etikett"></div>
<div class="mockup mockup--liquor" style="left:633px" role="img" aria-label="Flasche mit Kräuter-Etikett"></div>
<div class="mockup mockup--liquor" style="left:729px" role="img" aria-label="Flasche mit Johannisbeere-Etikett"></div>

<h2 class="section-title" style="top:429px">Whiskey:</h2>

<!-- whisky labels -->
<svg class="label whisky" style="left:50px;top:468px" viewBox="0 0 405 405" preserveAspectRatio="none">
  <rect x="1" y="1" width="403" height="403" fill="#fff" stroke="#888" stroke-width="2"/>
  <polygon points="0,0 405,0 405,248 0,318" fill="var(--coal)"/>
  <polygon points="30,318 405,262 405,290 30,345" fill="var(--mist)"/>
  <circle cx="202" cy="48" r="18" fill="#fff"/>
  <text x="202" y="105" text-anchor="middle" fill="#fff" font-size="17" font-weight="700" letter-spacing="3">HOLLBERG'S</text>
  <text class="script" x="45" y="235" fill="#fff" font-size="100" transform="rotate(-8 45 235)">Whiskey</text>
  <text class="script" x="150" y="280" fill="#fff" font-size="40" transform="rotate(-8 150 280)">dunkel</text>
  <text x="205" y="308" fill="#fff" font-size="20" transform="rotate(-8 205 308)">40 % VOL</text>
  <text x="372" y="282" text-anchor="end" fill="#fff" font-size="20" transform="rotate(-8 372 282)">0,2 L</text>
  <text x="202" y="362" text-anchor="middle" fill="var(--ink)" font-size="14">Edelbrände &amp; Liköre Konrad Hollberg</text>
  <text x="202" y="380" text-anchor="middle" fill="var(--ink)" font-size="14">Lindenweg 12 · D-97999 Auheim · Telefon 0 12 34 - 56 78</text>
</svg>

<svg class="label whisky" style="left:113px;top:521px" viewBox="0 0 405 405" preserveAspectRatio="none">
  <rect x="1" y="1" width="403" height="403" fill="#fff" stroke="#888" stroke-width="2"/>
  <polygon points="0,0 405,0 405,248 0,318" fill="var(--silver)"/>
  <polygon points="30,318 405,262 405,290 30,345" fill="var(--mist)"/>
  <circle cx="202" cy="48" r="18" fill="var(--ink)"/>
  <text x="202" y="105" text-anchor="middle" fill="var(--ink)" font-size="17" font-weight="700" letter-spacing="3">HOLLBERG'S</text>
  <text class="script" x="45" y="235" fill="var(--ink)" font-size="100" transform="rotate(-8 45 235)">Whiskey</text>
  <text class="script" x="165" y="280" fill="var(--ink)" font-size="40" transform="rotate(-8 165 280)">hell</text>
  <text x="205" y="308" fill="var(--ink)" font-size="20" transform="rotate(-8 205 308)">40 % VOL</text>
  <text x="372" y="282" text-anchor="end" fill="var(--ink)" font-size="20" transform="rotate(-8 372 282)">0,2 L</text>
  <text x="202" y="362" text-anchor="middle" fill="var(--ink)" font-size="14">Edelbrände &amp; Liköre Konrad Hollberg</text>
  <text x="202" y="380" text-anchor="middle" fill="var(--ink)" font-size="14">Lindenweg 12 · D-97999 Auheim · Telefon 0 12 34 - 56 78</text>
</svg>

<svg class="label whisky" style="left:192px;top:573px" viewBox="0 0 405 405" preserveAspectRatio="none">
  <rect x="1" y="1" width="403" height="403" fill="#fff" stroke="#888" stroke-width="2"/>
  <polygon points="0,0 405,0 405,248 0,318" fill="var(--slate)"/>
  <polygon points="30,318 405,262 405,290 30,345" fill="var(--mist)"/>
  <circle cx="202" cy="48" r="18" fill="#fff"/>
  <text x="202" y="105" text-anchor="middle" fill="#fff" font-size="17" font-weight="700" letter-spacing="3">HOLLBERG'S</text>
  <text class="script" x="45" y="235" fill="#fff" font-size="100" transform="rotate(-8 45 235)">Whiskey</text>
  <text class="script" x="100" y="278" fill="#fff" font-size="40" transform="rotate(-8 100 278)">Special Edition</text>
  <text x="205" y="308" fill="#fff" font-size="20" transform="rotate(-8 205 308)">40 % VOL</text>
  <text x="372" y="282" text-anchor="end" fill="#fff" font-size="20" transform="rotate(-8 372 282)">0,2 L</text>
  <text x="202" y="362" text-anchor="middle" fill="var(--ink)" font-size="14">Edelbrände &amp; Liköre Konrad Hollberg</text>
  <text x="202" y="380" text-anchor="middle" fill="var(--ink)" font-size="14">Lindenweg 12 · D-97999 Auheim · Telefon 0 12 34 - 56 78</text>
</svg>

<div class="mockup mockup--whisky" style="left:429px" role="img" aria-label="Whiskeyflasche mit Etikett dunkel"></div>
<div class="mockup mockup--whisky" style="left:557px" role="img" aria-label="Whiskeyflasche mit Etikett hell"></div>
<div class="mockup mockup--whisky" style="left:685px" role="img" aria-label="Whiskeyflasche mit Etikett Special Edition"></div>

<h2 class="section-title" style="top:805px">Whiskey:</h2>

<!-- gin label -->
<svg class="label gin" viewBox="0 0 550 550" preserveAspectRatio="none">
  <rect x="1" y="1" width="548" height="548" fill="#fff" stroke="#555" stroke-width="2"/>
  <circle cx="275" cy="80" r="34" fill="var(--gold)"/>
  <text x="275" y="160" text-anchor="middle" fill="#666" font-size="26" font-weight="700" letter-spacing="6">HOLLBERG'S</text>
  <polygon points="260,205 550,145 550,250" fill="var(--mist)"/>
  <polygon points="0,158 550,250 550,486 0,391" fill="var(--slate)"/>
  <polygon points="0,391 360,452 0,476" fill="var(--mist)"/>
  <text x="40" y="225" fill="#fff" font-size="38" transform="rotate(8 40 225)">HOLLBERG'S</text>
  <text class="script" x="175" y="395" fill="#fff" font-size="160" transform="rotate(-4 175 395)">Gin</text>
  <text x="492" y="420" text-anchor="end" fill="#fff" font-size="26" transform="rotate(8 492 420)">0,2 L</text>
  <text x="492" y="455" text-anchor="end" fill="#fff" font-size="26" transform="rotate(8 492 455)">40 % VOL</text>
  <text x="275" y="505" text-anchor="middle" fill="#444" font-size="18">Edelbrände &amp; Liköre Konrad Hollberg</text>
  <text x="275" y="527" text-anchor="middle" fill="#444" font-size="18">Lindenweg 12 · D-97999 Auheim · Telefon 0 12 34 - 56 78</text>
</svg>

<div class="mockup mockup--gin" role="img" aria-label="Ginflasche mit Korken und Gin-Etikett"></div>

</body>
</html>
```